Business Cards, Letterheads, Envelopes

A company's new identity to be reflected on its stationery items

Target Market(s)

Large Corporate Companies & Enterprises

Font styles to use
Sans Serif

Colors
0555a3
3176b5
85abd2
85cae6
33a6d7
0293ce

```html
<!DOCTYPE html>
<html lang="en">
<head>
<meta charset="utf-8">
<title>Corvane Nexus – Business Card</title>
<link rel="stylesheet" href="https://fonts.googleapis.com/css2?family=Roboto:wght@400;500;700&display=swap">
<style>
  :root {
    --bg: #e4e4e2;
    --white: #ffffff;
    --blue: #3176b5;
    --blue-bright: #3590d3;
    --blue-deep: #1f76b9;
    --ink: #555a60;
    --grey-block: #a9a9a9;
  }
  * { margin: 0; padding: 0; box-sizing: border-box; }
  html, body { width: 1200px; height: 801px; overflow: hidden; }
  body {
    background: var(--bg);
    font-family: "Roboto", Arial, sans-serif;
    position: relative;
  }
  .card {
    position: absolute;
    top: 252px;
    width: 525px;
    height: 300px;
    box-shadow: 0 6px 18px rgba(0,0,0,0.18);
    overflow: hidden;
  }
  /* Front */
  .card-front { left: 50px; background: var(--white); }
  .front-brand {
    position: absolute; top: 52px; left: 250px;
    display: flex; align-items: center; gap: 12px;
  }
  .brand-dot {
    width: 46px; height: 46px; border-radius: 50%;
    border: 3px solid var(--blue-bright);
    flex: none;
  }
  .brand-name {
    font-weight: 700; font-size: 21px; line-height: 1.05;
    letter-spacing: 1px; text-transform: uppercase;
    color: var(--blue-bright);
  }
  .holder { position: absolute; left: 34px; top: 124px; }
  .holder-name {
    font-weight: 700; font-size: 19px; line-height: 22px;
    color: var(--blue-bright);
    text-transform: uppercase; letter-spacing: 0.3px;
  }
  .holder-title {
    font-size: 14px; line-height: 18px; color: var(--ink);
    font-weight: 500; margin-bottom: 8px;
  }
  .contact-list { list-style: none; }
  .contact-list li {
    display: flex; align-items: center; gap: 7px;
    font-size: 11.5px; color: var(--ink); line-height: 17px;
  }
  .contact-list svg { width: 11px; height: 11px; fill: var(--blue-bright); flex: none; }
  .address {
    position: absolute; left: 330px; top: 196px;
    font-size: 12px; line-height: 16px; color: var(--ink);
  }
  .front-band {
    position: absolute; left: 0; top: 262px; width: 408px; height: 14px;
    background: var(--blue-bright);
  }
  .mini-dot {
    position: absolute; left: 416px; top: 246px;
    width: 30px; height: 30px; border-radius: 50%;
    border: 2px solid var(--blue-bright);
  }
  .grey-block {
    position: absolute; left: 455px; top: 232px; width: 70px; height: 14px;
    background: var(--grey-block);
  }
  /* Back */
  .card-back {
    left: 625px;
    background: linear-gradient(160deg, var(--blue-bright) 0%, #338fd2 55%, var(--blue-deep) 100%);
    display: flex; align-items: center; justify-content: center;
  }
  .back-brand { display: flex; align-items: center; gap: 18px; }
  .back-brand .brand-dot { width: 70px; height: 70px; border-color: var(--white); border-width: 4px; }
  .back-brand .brand-name { color: var(--white); font-size: 28px; }
</style>
</head>
<body>
  <section class="card card-front">
    <div class="front-brand">
      <span class="brand-dot"></span>
      <div class="brand-name">Corvane Nexus<br>Private Limited</div>
    </div>

    <div class="holder">
      <div class="holder-name">Daniel Arlo</div>
      <div class="holder-title">President</div>
      <ul class="contact-list">
        <li><svg viewBox="0 0 24 24"><path d="M6.6 10.8a15.1 15.1 0 006.6 6.6l2.2-2.2c.3-.3.7-.4 1-.2 1.1.4 2.3.6 3.6.6.6 0 1 .4 1 1V20c0 .6-.4 1-1 1A17 17 0 013 4c0-.6.4-1 1-1h3.5c.6 0 1 .4 1 1 0 1.3.2 2.5.6 3.6.1.3 0 .7-.2 1z"/></svg>555.014.2280</li>
        <li><svg viewBox="0 0 24 24"><path d="M6 2h12v6H6zM4 9h16a2 2 0 012 2v7h-4v4H6v-4H2v-7a2 2 0 012-2zm4 8v3h8v-3z"/></svg>555.014.2291</li>
        <li><svg viewBox="0 0 24 24"><path d="M2 5h20v14H2zm2 2v.5l8 5 8-5V7z"/></svg>danielarlo@corvanenexus.com</li>
        <li><svg viewBox="0 0 24 24"><circle cx="12" cy="12" r="10"/></svg>www.corvanenexus.com</li>
      </ul>
    </div>

    <p class="address">2275 Quarry Road Suite 410<br>Fairdale, MN 55990</p>

    <div class="front-band"></div>
    <span class="mini-dot"></span>
    <div class="grey-block"></div>
  </section>

  <section class="card card-back">
    <div class="back-brand">
      <span class="brand-dot"></span>
      <div class="brand-name">Corvane Nexus<br>Private Limited</div>
    </div>
  </section>
</body>
</html>
```